"Thank You" card for professional property management agency.

We need to create a DL size "Thank You" card primarily used to thank new clients for their business and referrals.
We are a real estate agency based on Sydney's Northern Beaches. We want the card to feel happy and professional, incorporating our logo.
See our website for details about our business - www.harbourlanerealty.com.au
We have attached our logo in black text and white text as well as some images we have used across our website.
One side must have the ability to hand write a message of thank you on.
I would like this to be a clean and simple design, feel free to use any image supplied, but we are also happy with plain or patterned designs too.

Target Market(s)

Property investors male and female aged 30-60

Industry/Entity Type

Real Estate

Font styles to use
Other font styles liked:
• Please let the designer choose font

Colors

Designer to choose colors to be used in the design.

Requirements
Must have
• DL Size: Full Bleed 213x102mm. Doc size 210x99mm (horizontal)
• Harbour Lane Realty Logo
• Contact Details:
• info@harbourlanerealty.com.au
• Tel: 0493 716 258
• Suite 3, 17 Wentmore Rd, Calderwood NSW 2118
• "Thank You" somewhere on the card
• Area or side to write message on.
• Design to be provided in editable photoshop PSD file and print ready PDF file
Nice to have
• Sleek professional design that feels "happy or grateful" as it is a thank you card
• Happy to use a plain colour or pattern on one side - it does not have to be an image provided, but feel free to design with either.
Should not have
• should not be too busy, keep it clean and simple.

```html
<!DOCTYPE html>
<html lang="en">
<head>
<meta charset="utf-8">
<title>Harbour Lane Realty – Thank You Card</title>
<link rel="stylesheet" href="https://fonts.googleapis.com/css2?family=Roboto+Slab:wght@700;800&family=Open+Sans:wght@400;600&display=swap">
<style>
  :root {
    --teal: #1f8d9b;
    --teal-deep: #166e7b;
    --teal-light: #3fb0ba;
    --stone: #6b5d5c;
    --paper: #ffffff;
    --backdrop: #e9ecee;
    --sky: #8ec9ea;
    --foliage: #5f7f55;
    --facade: #cfd3d4;
  }
  * { margin: 0; padding: 0; box-sizing: border-box; }
  html, body { width: 1200px; height: 884px; overflow: hidden; }
  body { background: var(--backdrop); position: relative; }

  .card {
    position: absolute;
    left: 50px; top: 182px;
    width: 1100px; height: 519px;
    background: var(--paper);
    overflow: hidden;
    box-shadow: 0 6px 24px rgba(0,0,0,0.12);
  }
  .card__shapes { position: absolute; inset: 0; width: 100%; height: 100%; }

  .card__headline {
    position: absolute;
    left: 44px; top: 282px;
    font-family: "Roboto Slab", Georgia, serif;
    font-weight: 800;
    font-size: 54px;
    line-height: 1.2;
    letter-spacing: 1px;
    color: var(--paper);
    transform: rotate(-3deg);
    transform-origin: left center;
    white-space: nowrap;
  }

  .brand {
    position: absolute;
    left: 490px; top: 205px;
    display: flex; align-items: center; gap: 16px;
  }
  .brand__square { width: 96px; height: 96px; background: var(--stone); flex: none; }
  .brand__name {
    font-family: "Roboto Slab", Georgia, serif;
    font-weight: 700;
    font-size: 21px;
    line-height: 1.2;
    color: var(--stone);
    text-transform: uppercase;
    white-space: nowrap;
  }

  .contact {
    position: absolute;
    right: 40px; top: 232px;
    text-align: right;
    font-family: "Open Sans", Arial, sans-serif;
    font-style: normal;
    font-weight: 400;
    font-size: 18px;
    line-height: 1.35;
    color: var(--teal);
    white-space: nowrap;
  }
  .contact__email {
    position: absolute;
    right: 40px; top: 364px;
    font-family: "Open Sans", Arial, sans-serif;
    font-weight: 400;
    font-size: 18px;
    color: var(--teal);
    white-space: nowrap;
  }
</style>
</head>
<body>
  <main class="card">
    <svg class="card__shapes" viewBox="0 0 1100 519" preserveAspectRatio="none">
      <defs>
        <linearGradient id="photoTones" x1="0" y1="0" x2="0" y2="1">
          <stop offset="0" stop-color="var(--sky)"/>
          <stop offset="0.45" stop-color="var(--facade)"/>
          <stop offset="1" stop-color="var(--foliage)"/>
        </linearGradient>
      </defs>
      <polygon class="photo-area" role="img" aria-label="Photo of modern townhouses with gardens under a blue sky"
               points="0,0 760,0 610,235 470,250 0,110" fill="url(#photoTones)"/>
      <polygon class="band band--thin" points="0,120 480,258 480,266 0,132" fill="var(--teal)"/>
      <polygon class="band band--main" points="0,148 560,300 0,470" fill="var(--teal)"/>
      <polygon class="band band--light" points="0,490 575,308 615,312 170,519 0,519" fill="var(--teal-light)"/>
      <polygon class="corner corner--deep" points="900,0 1100,0 1100,170" fill="var(--teal-deep)"/>
      <polygon class="corner corner--light" points="850,0 880,0 1100,195 1100,215" fill="var(--teal-light)"/>
    </svg>

    <h1 class="card__headline">THANK YOU</h1>

    <div class="brand">
      <span class="brand__square"></span>
      <span class="brand__name">Harbour Lane<br>Realty</span>
    </div>

    <address class="contact">
      Suite 3, 17 Wentmore Rd,<br>
      Calderwood NSW 2118<br>
      Tel: 0493 716 258
    </address>
    <p class="contact__email">Email: info@harbourlanerealty.com.au</p>
  </main>
</body>
</html>
```